Lumex.CI Portal Application Design

** See the attached treatment PDF document with complete details, but here are the broad points:**

We need designs for a login screen and three very similar interior page screens. Because the app requires a CodeNest, RepoKeep or Stackpail account to login, screen shots are attached to this treatment. Please review those for the designs needed.
- Login Page
- Project Index page (with sidebar tabs for other options. Those specific pages do not need to be coded once we have the template).
- Project build list. A list of the builds available per project
- Build details. This shows the build steps and results of the build steps.

The site should be visually compatible with https://lumexweb.example-host.net. The same logo and color scheme (logo attached)

General templates are desired that we can build on.

There is a significant bonus tip involved if you’re willing to provide a toggle for a light and a dark mode. I do not know what this would look like but feel free to present proposals.

Industry/Entity Type

Continuous Integration/Testing (think LoopForge, KestrelCI)

Coding

Coded - Design and coding required

Number of Pages Required

1 page

Font styles to use
Sans Serif
Other font styles liked:
• Roboto

Colors
0054AA
0677BA
7BADD7
CADEEF
E8F1F8
FFC000
F8CF3A
FAE287
FDF2CF
FEFAEE

Requirements
Nice to have
• Light and Dark Mode

```html
<!DOCTYPE html>
<html lang="en">
<head>
<meta charset="utf-8">
<title>Lumex.CI — Build Details</title>
<link href="https://fonts.googleapis.com/css2?family=Roboto:wght@400;500;700&display=swap" rel="stylesheet">
<style>
:root{
  --bg:#10224a;
  --bg-deep:#0c1c3f;
  --header:#15264d;
  --crumb:#2c3b5f;
  --panel:#0d1f43;
  --panel-line:#2f4068;
  --card:#0f2247;
  --card-active:#1d2d53;
  --card-line:#34466e;
  --pill:#a0a4b6;
  --pill-dark:#5c6580;
  --text:#ffffff;
  --muted:#c9cfdd;
  --dot:#8d96ad;
  --yellow:#ffc000;
  --yellow-light:#f8cf3a;
}
*{box-sizing:border-box;margin:0;padding:0}
html,body{width:1200px;height:969px;overflow:hidden}
body{
  font-family:"Roboto",sans-serif;color:var(--text);position:relative;
  background:radial-gradient(circle at 95% 95%,#2a3a62 0,transparent 30%),
             linear-gradient(180deg,#14264f 0%,var(--bg) 50%,#15274f 100%);
}
.header{position:absolute;left:0;top:0;width:1200px;height:74px;background:var(--header)}
.brand{position:absolute;left:39px;top:20px;display:flex;align-items:center;gap:10px}
.brand-mark{width:34px;height:34px;border-radius:50%;background:#8e94a8}
.brand-name{font-size:23px;font-weight:700}
.storage{position:absolute;left:265px;top:31px;font-size:12px;font-weight:500}
.upgrade{position:absolute;left:502px;top:26px;width:101px;height:27px;border-radius:14px;background:var(--pill-dark);font-size:12px;font-weight:700;display:flex;align-items:center;justify-content:center}
.menu{position:absolute;left:1023px;top:30px;width:27px}
.menu span{display:block;height:2px;background:#9aa3bb;margin-bottom:6px}
.mode-toggle{position:absolute;left:1078px;top:25px;width:60px;height:29px;border-radius:15px;background:#9ea3b6}
.mode-knob{position:absolute;left:3px;top:3px;width:23px;height:23px;border-radius:50%;background:#fff}
.breadcrumb{position:absolute;left:0;top:74px;width:1200px;height:29px;background:var(--crumb);font-size:13px;display:flex;align-items:center;padding-left:43px;gap:8px}
.breadcrumb b{font-weight:500}
.breadcrumb i{font-style:normal;color:#c9cfdd;font-size:11px}
.page-title{position:absolute;left:44px;top:128px;font-size:33px;font-weight:700}
.sidebar{position:absolute;left:32px;top:201px;width:205px}
.side-item{display:flex;align-items:center;gap:12px;height:45px;padding-left:18px;font-size:17px;font-weight:500}
.side-item.active{background:var(--pill);border-radius:23px 0 0 23px;padding-left:17px}
.side-item.assets{margin-top:17px;padding-left:18px}
.side-item.tokens{margin-top:10px}
.panel{position:absolute;left:237px;top:185px;width:915px;height:693px;background:var(--panel);border:1px solid var(--panel-line);border-radius:6px}
.build-title{position:absolute;left:33px;top:24px;font-size:21px;font-weight:700}
.actions{position:absolute;left:36px;top:62px;display:flex;gap:17px;font-size:11.5px;font-weight:500}
.actions span,.meta span{display:flex;align-items:center;gap:4px}
.meta{position:absolute;left:36px;top:95px;display:flex;gap:20px;font-size:11px;font-weight:500}
.view-site{position:absolute;left:731px;top:31px;width:151px;height:30px;border-radius:15px;background:var(--yellow);font-size:11.5px;font-weight:700;display:flex;align-items:center;justify-content:center;gap:5px}
.advanced{position:absolute;left:734px;top:71px;width:151px;height:28px;border-radius:14px;background:var(--pill-dark);font-size:11px;color:#e0e3ec;display:flex;align-items:center;justify-content:center;gap:4px}
.timeline{position:absolute;left:39px;top:164px;width:2px;height:399px;border-left:2px dotted var(--dot)}
.node{position:absolute;left:34px;width:12px;height:12px;border-radius:50%;border:3px solid var(--dot);background:var(--panel)}
.task{position:absolute;left:62px;width:823px;height:71px;border:1px solid var(--card-line);border-radius:5px;background:var(--card)}
.task.active{background:var(--card-active)}
.task h3{position:absolute;left:23px;top:13px;font-size:16px;font-weight:700}
.task p{position:absolute;left:23px;top:43px;font-size:10.5px;font-weight:500;display:flex;align-items:center;gap:9px}
.chev{position:absolute;right:22px;top:20px;width:30px;height:30px;border-radius:50%;background:#2e3d62;display:flex;align-items:center;justify-content:center}
.support{position:absolute;left:1035px;top:898px;width:128px;height:37px;border-radius:19px;background:var(--yellow);font-size:13px;font-weight:700;display:flex;align-items:center;justify-content:center;gap:6px}
</style>
</head>
<body>
<header class="header">
  <div class="brand"><div class="brand-mark"></div><span class="brand-name">Lumex.CI</span></div>
  <div class="storage">LumexCi is using 8.60 GB out of 500 GB.</div>
  <div class="upgrade">Upgrade now!</div>
  <div class="menu"><span></span><span></span><span></span></div>
  <div class="mode-toggle"><div class="mode-knob"></div>
    <svg style="position:absolute;left:38px;top:8px" width="13" height="13" viewBox="0 0 12 12"><circle cx="6" cy="6" r="2.5" fill="#fff"/><g stroke="#fff" stroke-width="1"><path d="M6 0v2M6 10v2M0 6h2M10 6h2M1.8 1.8l1.4 1.4M8.8 8.8l1.4 1.4M1.8 10.2l1.4-1.4M8.8 3.2l1.4-1.4"/></g></svg>
    <svg style="position:absolute;left:8px;top:8px" width="13" height="13" viewBox="0 0 12 12"><path d="M8 1a5 5 0 1 0 3 8A4 4 0 0 1 8 1z" fill="none" stroke="#1a2a50" stroke-width="1.3"/></svg>
  </div>
</header>
<nav class="breadcrumb"><b>LumexCI</b><i>›</i><span>lumex_test</span><i>›</i><span>Build Details</span></nav>
<h1 class="page-title">Build Steps</h1>

<aside class="sidebar">
  <div class="side-item active"><svg width="26" height="22" viewBox="0 0 26 22"><g fill="#fff"><rect x="9" y="1" width="8" height="7"/><rect x="2" y="9" width="8" height="6"/><rect x="11" y="9" width="8" height="6"/><rect x="2" y="15" width="8" height="6"/><rect x="11" y="15" width="8" height="6"/><rect x="19" y="13" width="6" height="8"/></g></svg>Builds</div>
  <div class="side-item assets"><svg width="26" height="26" viewBox="0 0 26 26"><circle cx="13" cy="13" r="11" fill="none" stroke="#9aa3bb" stroke-width="2" stroke-dasharray="3 2"/><circle cx="13" cy="13" r="5" fill="#9aa3bb"/></svg>Build Assets</div>
  <div class="side-item tokens"><svg width="26" height="24" viewBox="0 0 26 24"><path d="M5 10V3h16v7M13 21V8M9 12l4-4 4 4" fill="none" stroke="#9aa3bb" stroke-width="2"/></svg>Upload Tokens</div>
</aside>

<main class="panel">
  <h2 class="build-title">Testing Phyr 8.5 Container</h2>
  <div class="actions">
    <span><svg width="18" height="10" viewBox="0 0 18 10"><circle cx="9" cy="5" r="3.5" fill="none" stroke="#fff" stroke-width="2"/><path d="M0 5h5M13 5h5" stroke="#fff" stroke-width="2"/></svg>Commit 55e6a6</span>
    <span><svg width="12" height="16" viewBox="0 0 12 16"><g fill="none" stroke="#fff" stroke-width="1.4"><circle cx="3" cy="3" r="2"/><circle cx="3" cy="13" r="2"/><circle cx="9" cy="4" r="2"/><path d="M3 5v6M9 6c0 4-6 3-6 5"/></g></svg>View pull request</span>
    <span><svg width="12" height="12" viewBox="0 0 12 12"><circle cx="6" cy="6" r="5" fill="none" stroke="#fff" stroke-width="1.5"/></svg>View branch</span>
    <span><svg width="14" height="14" viewBox="0 0 14 14"><path d="M6 8l2-2M5 5l2-2a2.5 2.5 0 0 1 4 4l-2 2M9 9l-2 2a2.5 2.5 0 0 1-4-4l2-2" fill="none" stroke="#fff" stroke-width="1.3"/></svg>View build permalink</span>
    <span><svg width="14" height="14" viewBox="0 0 14 14"><path d="M2 7a5 5 0 0 1 9-3M12 7a5 5 0 0 1-9 3M11 1v3H8M3 13v-3h3" fill="none" stroke="#fff" stroke-width="1.3"/></svg>Rebuild</span>
    <span><svg width="10" height="14" viewBox="0 0 10 14"><path d="M2 1h6M3 1v6H1h8H7V1M5 7v6" fill="none" stroke="#fff" stroke-width="1.3"/></svg>Pin</span>
    <span><svg width="11" height="12" viewBox="0 0 11 12"><path d="M1 1h9v10H1zM4 3v6M7 3v6" fill="none" stroke="#fff" stroke-width="1.2"/></svg>Delete</span>
  </div>
  <div class="meta">
    <span><svg width="14" height="10" viewBox="0 0 14 10"><rect x="1" y="2" width="12" height="7" rx="2" fill="none" stroke="#fff" stroke-width="1.3"/><path d="M3 6h8" stroke="#fff"/></svg>DISK SPACE: 626.7 MB</span>
    <span><svg width="11" height="11" viewBox="0 0 11 11"><circle cx="5.5" cy="5.5" r="5" fill="#fff"/><path d="M5.5 2.5v3h2" stroke="#0d1f43" stroke-width="1.2" fill="none"/></svg>BUILT: November1, 2025 6:50PM</span>
  </div>
  <div class="view-site">VIEW SITE <svg width="6" height="9" viewBox="0 0 6 9"><path d="M1 1l3.5 3.5L1 8" fill="none" stroke="#fff" stroke-width="1.6"/></svg></div>
  <div class="advanced">Advanced Functions <svg width="8" height="6" viewBox="0 0 8 6"><path d="M1 1l3 3 3-3" fill="none" stroke="#fff" stroke-width="1.5"/></svg></div>

  <div class="timeline"></div>
  <div class="node" style="top:158px"></div>
  <div class="node" style="top:249px"></div>
  <div class="node" style="top:320px"></div>
  <div class="node" style="top:400px"></div>
  <div class="node" style="top:476px"></div>
  <div class="node" style="top:557px"></div>

  <section class="task active" style="top:141px"><h3>CodeNestDownloader task</h3><p><svg width="11" height="11" viewBox="0 0 11 11"><circle cx="5.5" cy="5.5" r="5" fill="#fff"/><path d="M5.5 2.5v3h2" stroke="#1d2d53" stroke-width="1.2" fill="none"/></svg>DURATION: 1 seconds 165 miliseconds</p><div class="chev"><svg width="12" height="8" viewBox="0 0 12 8"><path d="M1 1l5 5 5-5" fill="none" stroke="#fff" stroke-width="2"/></svg></div></section>
  <section class="task" style="top:218px"><h3>AssetDownloader task</h3><p><svg width="11" height="11" viewBox="0 0 11 11"><circle cx="5.5" cy="5.5" r="5" fill="#fff"/><path d="M5.5 2.5v3h2" stroke="#0f2247" stroke-width="1.2" fill="none"/></svg>DURATION: 1 seconds 165 miliseconds</p><div class="chev"><svg width="12" height="8" viewBox="0 0 12 8"><path d="M1 1l5 5 5-5" fill="none" stroke="#fff" stroke-width="2"/></svg></div></section>
  <section class="task" style="top:294px"><h3>Database task</h3><p><svg width="11" height="11" viewBox="0 0 11 11"><circle cx="5.5" cy="5.5" r="5" fill="#fff"/><path d="M5.5 2.5v3h2" stroke="#0f2247" stroke-width="1.2" fill="none"/></svg>DURATION: 1 seconds 165 miliseconds</p><div class="chev"><svg width="12" height="8" viewBox="0 0 12 8"><path d="M1 1l5 5 5-5" fill="none" stroke="#fff" stroke-width="2"/></svg></div></section>
  <section class="task" style="top:372px"><h3>Searchlite task</h3><p><svg width="11" height="11" viewBox="0 0 11 11"><circle cx="5.5" cy="5.5" r="5" fill="#fff"/><path d="M5.5 2.5v3h2" stroke="#0f2247" stroke-width="1.2" fill="none"/></svg>DURATION: 1 seconds 165 miliseconds</p><div class="chev"><svg width="12" height="8" viewBox="0 0 12 8"><path d="M1 1l5 5 5-5" fill="none" stroke="#fff" stroke-width="2"/></svg></div></section>
  <section class="task" style="top:451px"><h3>ScriptRun task</h3><p><svg width="11" height="11" viewBox="0 0 11 11"><circle cx="5.5" cy="5.5" r="5" fill="#fff"/><path d="M5.5 2.5v3h2" stroke="#0f2247" stroke-width="1.2" fill="none"/></svg>DURATION: 1 seconds 165 miliseconds</p><div class="chev"><svg width="12" height="8" viewBox="0 0 12 8"><path d="M1 1l5 5 5-5" fill="none" stroke="#fff" stroke-width="2"/></svg></div></section>
  <section class="task" style="top:530px"><h3>Testing</h3><p><svg width="11" height="11" viewBox="0 0 11 11"><circle cx="5.5" cy="5.5" r="5" fill="#fff"/><path d="M5.5 2.5v3h2" stroke="#0f2247" stroke-width="1.2" fill="none"/></svg>DURATION: 1 seconds 165 miliseconds</p><div class="chev"><svg width="12" height="8" viewBox="0 0 12 8"><path d="M1 1l5 5 5-5" fill="none" stroke="#fff" stroke-width="2"/></svg></div></section>
</main>

<div class="support"><svg width="22" height="20" viewBox="0 0 22 20"><path d="M3 10a8 8 0 0 1 16 0" fill="none" stroke="#fff" stroke-width="2"/><rect x="1" y="9" width="4" height="6" rx="1.5" fill="#fff"/><rect x="17" y="9" width="4" height="6" rx="1.5" fill="#fff"/><circle cx="11" cy="11" r="4.5" fill="#fff"/></svg>SUPPORT</div>
</body>
</html>
```